Design some Business Cards

***WINNER MUST PROVIDE LAYERED PSD FILE(S)***

This is for a business that is about to launch and needs a GREAT business card design.

You can see the website draft here: http://kovta812.client.ferntop583.com/

Use the website to help understand how the look and feel of the cards should be and get ideas for the design.

The slogan is "Smart Property Growth With a Single Click"

Logo is attached

Winner will also get a chance to design:

Flyer
Vertical Banner
Trade Show (Expo) Display
Brochure

Good Luck!

```html
<!DOCTYPE html>
<html lang="en">
<head>
<meta charset="utf-8">
<title>kovta812 business cards</title>
<link rel="stylesheet" href="https://fonts.googleapis.com/css2?family=Roboto:wght@400;500;700&display=swap">
<style>
  :root {
    --backdrop: #e9e9eb;
    --card-dark: #151515;
    --card-dark-edge: #2a2a2a;
    --card-light: #ffffff;
    --brand-red: #d7282f;
    --ink: #3a3a3a;
    --ink-soft: #5a5a5a;
    --on-dark: #f4f4f4;
  }
  * { margin: 0; padding: 0; box-sizing: border-box; }
  html, body { width: 1200px; height: 800px; overflow: hidden; }
  body {
    background: var(--backdrop);
    font-family: "Roboto", Arial, sans-serif;
    position: relative;
  }
  .card {
    position: absolute;
    top: 246px;
    width: 540px;
    height: 309px;
    box-shadow: 0 6px 18px rgba(0,0,0,0.18);
  }
  .card--front {
    left: 45px;
    background: radial-gradient(ellipse at 50% 45%, var(--card-dark-edge) 0%, var(--card-dark) 70%);
  }
  .card--back {
    left: 615px;
    background: var(--card-light);
  }
  .brand {
    display: flex;
    align-items: center;
    gap: 10px;
    font-weight: 400;
    letter-spacing: 0.5px;
    white-space: nowrap;
  }
  .brand__mark {
    width: 14px;
    height: 14px;
    background: var(--brand-red);
  }
  .card--front .brand {
    position: absolute;
    top: 100px;
    left: 0;
    right: 0;
    justify-content: center;
    font-size: 58px;
    color: var(--on-dark);
  }
  .card--front .tagline {
    position: absolute;
    top: 182px;
    left: 0;
    right: 0;
    text-align: center;
    font-size: 11px;
    letter-spacing: 0.6px;
    color: var(--on-dark);
    text-transform: uppercase;
    white-space: nowrap;
  }
  .card--back .brand {
    position: absolute;
    top: 40px;
    right: 46px;
    font-size: 40px;
    color: var(--ink);
  }
  .card--back .tagline {
    position: absolute;
    top: 103px;
    right: 46px;
    font-size: 9.5px;
    letter-spacing: 0.4px;
    color: var(--brand-red);
    text-transform: uppercase;
    white-space: nowrap;
  }
  .rule {
    position: absolute;
    height: 2px;
    background: var(--brand-red);
  }
  .rule--tagline { top: 118px; left: 262px; right: 46px; }
  .rule--name { top: 170px; left: 32px; width: 310px; }
  .person {
    position: absolute;
    top: 138px;
    left: 32px;
  }
  .person__name {
    font-size: 15px;
    font-weight: 700;
    text-transform: uppercase;
    color: var(--ink);
    letter-spacing: 0.3px;
  }
  .person__name span { color: var(--brand-red); }
  .person__role {
    font-size: 10.5px;
    color: var(--ink-soft);
    margin-top: 1px;
  }
  .address {
    position: absolute;
    top: 138px;
    left: 366px;
    display: flex;
    gap: 10px;
    font-size: 11.5px;
    line-height: 1.3;
    color: var(--ink);
  }
  .contacts {
    position: absolute;
    top: 198px;
    left: 32px;
    list-style: none;
  }
  .contacts li {
    display: flex;
    align-items: center;
    gap: 12px;
    font-size: 11.5px;
    color: var(--ink);
    height: 24px;
  }
  .icon { width: 13px; height: 13px; flex: none; }
  .icon path, .icon circle { fill: var(--brand-red); }
  .icon .stroke { fill: none; stroke: var(--brand-red); stroke-width: 1.4; }
  .icon .stroke--light { stroke: var(--card-light); }
</style>
</head>
<body>

<section class="card card--front" aria-label="Card front">
  <div class="brand"><span class="brand__mark"></span>kovta812</div>
  <p class="tagline">Smart Property Growth With a Single Click</p>
</section>

<section class="card card--back" aria-label="Card back">
  <div class="brand"><span class="brand__mark"></span>kovta812</div>
  <p class="tagline">Smart Property Growth With a Single Click</p>
  <div class="rule rule--tagline"></div>

  <div class="person">
    <p class="person__name"><span>Daniel</span> Moore</p>
    <p class="person__role">General Manager</p>
  </div>
  <div class="rule rule--name"></div>

  <div class="address">
    <svg class="icon" viewBox="0 0 16 16" aria-hidden="true">
      <path d="M8 0a5.5 5.5 0 0 0-5.5 5.5C2.5 9.6 8 16 8 16s5.5-6.4 5.5-10.5A5.5 5.5 0 0 0 8 0zm0 8a2.4 2.4 0 1 1 0-4.8A2.4 2.4 0 0 1 8 8z"/>
    </svg>
    <p>Your Street Address<br>United State, 12345</p>
  </div>

  <ul class="contacts">
    <li>
      <svg class="icon" viewBox="0 0 16 16" aria-hidden="true">
        <path d="M3.6 1.2 5.8 3.4c.4.4.4 1 0 1.4L4.7 5.9a9.5 9.5 0 0 0 5.4 5.4l1.1-1.1c.4-.4 1-.4 1.4 0l2.2 2.2c.4.4.4 1 0 1.4l-1.2 1.2c-.9.9-2.3 1-3.4.4A17 17 0 0 1 1.4 6.6C.8 5.5.9 4.1 1.8 3.2L3 2c.2-.4.4-.8.6-.8z"/>
      </svg>
      +123 456 7890
    </li>
    <li>
      <svg class="icon" viewBox="0 0 16 16" aria-hidden="true">
        <path d="M0 3h16v10H0z"/>
        <path d="M1.5 4.2 8 9l6.5-4.8" class="stroke stroke--light"/>
      </svg>
      john@youremail.com
    </li>
    <li>
      <svg class="icon" viewBox="0 0 16 16" aria-hidden="true">
        <circle cx="8" cy="8" r="7" class="stroke"/>
        <path class="stroke" d="M1 8h14M8 1c-2.5 2.5-2.5 11.5 0 14M8 1c2.5 2.5 2.5 11.5 0 14"/>
      </svg>
      www.yourwebsite.com
    </li>
  </ul>
</section>

</body>
</html>
```